Creative Labels needed for Hollow Cleaning Products

Four bottle labels 5.25 inches tall by 7 inches wide, Two packaging labels 4.375 inches tall by 4.5 inches wide. Basic Information on each labels including basic color scheme is attached - ok to change color scheme. Would like to add the words "Hollow Cleaning" somewhere on the two packaging labels and have the overall design hint at craft beer, perhaps something along the lines of Kiv Beer Labels (picture of this is attached) with a feminine touch and perhaps just a hint of the east (India/yoga/essential oils) and nature (plants/flowers). All labels will also need barcodes which are attached. Please make sure correct barcode is on correct label. The "packaging label barcode" is used twice - the same barcode on the two different "packaging" labels. All art is on clear background, so to my understanding all art and fonts need a white layer underneath.

Target Market(s)

age - 20s - 60s
location - urban
gender - all
income level - 40K and up
marital or family status - any
occupation - any
ethnic background - any
interests - natural health and wellness, yoga, essential oils, health food, craft beer, music, art, travel

Industry/Entity Type

Cleaning Product

Font styles to use
Decorative

Colors

Designer to choose colors to be used in the design.

Requirements
Must have
• See description. Please note there are 6 different labels. They will all have the same look, and there are only 2 different sizes involved. There are distinctions between each label as noted in the pictures submitted. Open to some budget adjustments if discussed/needed because of these 6 variations.
Nice to have
• See description, plus some clear space on the labels, as they will be printed on clear labels and placed on clear bottles.

```html
<!DOCTYPE html>
<html lang="en">
<head>
<meta charset="utf-8">
<title>Hollow Cleaning – Multi-Purpose Household Cleaner Package Label</title>
<link rel="stylesheet" href="https://fonts.googleapis.com/css2?family=Alfa+Slab+One&family=Arvo:wght@700&family=Dancing+Script&family=Roboto+Condensed:wght@400;700&display=swap">
<style>
  :root {
    --teal: #4bbac4;
    --brown: #6b3a3c;
    --white: #ffffff;
    --grey: #6e6e6e;
    --petal: #f3e6e4;
  }
  * { margin: 0; padding: 0; box-sizing: border-box; }
  html, body { width: 1200px; height: 1167px; overflow: hidden; background: var(--white); }
  .label {
    position: relative; width: 1200px; height: 1167px;
    background: var(--teal); overflow: hidden;
    font-family: "Arvo", serif; color: var(--brown);
  }
  .stripes-top {
    position: absolute; left: 0; top: 0; width: 100%; height: 71px;
    background: repeating-linear-gradient(90deg, var(--brown) 0 9px, var(--teal) 9px 17px);
  }
  .floral {
    position: absolute; left: 204px; top: 18px; width: 792px; height: 275px;
    border-radius: 50% 50% 40% 40%;
    background: radial-gradient(ellipse at center, var(--petal) 0%, #c99a98 55%, rgba(107,58,60,0) 75%);
  }
  .seal {
    position: absolute; left: 489px; top: 36px; width: 222px; height: 222px;
    border-radius: 50%; background: var(--white);
    border: 4px solid var(--brown);
    display: flex; align-items: center; justify-content: center; text-align: center;
    font-family: "Arvo", serif; font-weight: 700; font-size: 30px; line-height: 1.1;
    color: var(--brown);
  }
  .base-note {
    position: absolute; left: 0; width: 100%; top: 268px; text-align: center;
    color: var(--white); font-size: 20px; line-height: 22px; letter-spacing: 0.5px;
  }
  .title-small {
    position: absolute; left: 0; width: 100%; top: 352px; text-align: center;
    font-family: "Alfa Slab One", serif; font-size: 54px; letter-spacing: 1px;
  }
  .title-big {
    position: absolute; left: 0; width: 100%; text-align: center;
    font-family: "Alfa Slab One", serif; font-size: 106px; line-height: 1;
  }
  .title-big.line1 { top: 430px; }
  .title-big.line2 { top: 528px; }
  .make-own {
    position: absolute; left: 447px; top: 667px; width: 306px; height: 53px;
    background: var(--brown); color: var(--white);
    font-family: "Dancing Script", cursive; font-size: 38px;
    display: flex; align-items: center; justify-content: center;
  }
  .tagline {
    position: absolute; left: 0; width: 100%; top: 738px; text-align: center;
    color: var(--white); font-family: "Dancing Script", cursive; font-size: 36px; line-height: 35px;
  }
  .savings {
    position: absolute; left: 456px; top: 860px; width: 288px; height: 100px;
    border: 2px solid var(--white);
  }
  .savings .blossom {
    position: absolute; left: 12px; top: 15px; width: 72px; height: 72px; border-radius: 50%;
    background: radial-gradient(circle, #c99a98 0%, var(--petal) 60%);
  }
  .savings .times {
    position: absolute; left: 96px; top: 2px; width: 186px; text-align: center;
    font-family: "Roboto Condensed", sans-serif; font-weight: 700; font-size: 48px; line-height: 50px;
  }
  .savings .note {
    position: absolute; left: 96px; top: 54px; width: 186px; text-align: center;
    font-family: "Roboto Condensed", sans-serif; font-weight: 700; font-size: 19px; line-height: 20px;
  }
  .claims {
    position: absolute; left: 302px; top: 1000px; width: 603px; height: 53px;
    border-top: 2px solid var(--white); border-bottom: 2px solid var(--white);
    color: var(--white); font-family: "Roboto Condensed", sans-serif; font-weight: 700;
    font-size: 41px; letter-spacing: 1px; text-align: center; line-height: 49px;
  }
  .maker {
    position: absolute; left: 31px; top: 1049px; transform-origin: 0 0; transform: rotate(-90deg);
    white-space: nowrap; font-family: "Roboto Condensed", sans-serif; font-size: 16px; color: var(--brown);
  }
  .code-panel { position: absolute; left: 957px; top: 740px; width: 243px; height: 340px; background: var(--white); }
  .footer-band { position: absolute; left: 0; top: 1075px; width: 100%; height: 65px; background: var(--white); }
  .yield {
    position: absolute; left: 244px; top: 1094px; white-space: nowrap;
    font-family: "Roboto Condensed", sans-serif; font-weight: 700; font-size: 29px; color: var(--brown);
  }
  .label-kind {
    position: absolute; left: 980px; top: 1070px; width: 218px; text-align: center;
    font-family: "Roboto Condensed", sans-serif; font-size: 19px; line-height: 22px; color: var(--grey);
  }
  .stripes-bottom {
    position: absolute; left: 0; top: 1140px; width: 100%; height: 27px;
    background: repeating-linear-gradient(90deg, var(--teal) 0 9px, var(--white) 9px 17px);
  }
</style>
</head>
<body>
<main class="label">
  <div class="stripes-top"></div>
  <div class="floral" role="img" aria-label="Engraved blossom branches framing the brand seal"></div>
  <div class="seal">Hollow<br>Cleaning</div>
  <p class="base-note">UNSCENTED<br>BASE<br>SUPER-CONCENTRATE</p>
  <h2 class="title-small">MULTI-PURPOSE</h2>
  <h1 class="title-big line1">HOUSEHOLD</h1>
  <h1 class="title-big line2">CLEANER</h1>
  <div class="make-own">Make Your Own</div>
  <p class="tagline">Just add water for<br>a streak-free shine,<br>naturally!</p>
  <div class="savings">
    <div class="blossom" role="img" aria-label="Small blossom illustration"></div>
    <div class="times">16x</div>
    <div class="note">CONCENTRATE FOR<br>INCREDIBLE SAVINGS</div>
  </div>
  <div class="claims">SAFE, NON TOXIC, PLANT BASED</div>
  <div class="maker">MADE BY BRIGHTFERN, INC. IN MILLBROOK, NJ.</div>
  <div class="code-panel"></div>
  <div class="footer-band"></div>
  <div class="yield">MAKES 16 BOTTLES OF READY-TO-USE HOUSEHOLD CLEANER</div>
  <div class="label-kind">THIS IS PACKAGE<br>LABEL</div>
  <div class="stripes-bottom"></div>
</main>
</body>
</html>
```